Re-design of Business Card

We require a design for our business card.

Korrim is a supplier of industrial packaging specializing in plastic products. We are undergoing a rebranding to appear more corporate. We have changed our company name to korrim and have a new logo.

I have uploaded our old card design with the previous company name.
Don't copy the current design. We are looking for a new design.

Industry/Entity Type

Manufacturing

Contact Information for Business Card

please don't copy the current design. we are looking for a new design.

Font styles to use
Sans Serif

Colors

Designer to choose colors to be used in the design.

Requirements
Must have
• clean and easy to read.

```html
<!DOCTYPE html>
<html lang="en">
<head>
<meta charset="utf-8">
<title>Korrim Business Card</title>
<link rel="stylesheet" href="https://fonts.googleapis.com/css2?family=Jost:wght@400;600&family=Poppins:wght@800&display=swap">
<style>
  :root {
    --stage: #e56a1f;
    --brand-orange: #ef7a22;
    --card-black: #0a0b0b;
    --card-white: #ffffff;
  }
  * { margin: 0; padding: 0; box-sizing: border-box; }
  html, body {
    width: 1200px;
    height: 1200px;
    overflow: hidden;
    background: var(--stage);
  }
  .canvas {
    width: 1200px;
    height: 1200px;
    display: flex;
    flex-direction: column;
    align-items: center;
    justify-content: center;
    gap: 60px;
  }
  .card {
    width: 700px;
    height: 400px;
    position: relative;
  }
  .card-back {
    background: var(--card-black);
    display: flex;
    align-items: center;
    justify-content: center;
  }
  .brand-name {
    display: flex;
    align-items: center;
    gap: 22px;
    font-family: "Jost", sans-serif;
    font-weight: 600;
    font-size: 96px;
    letter-spacing: 4px;
    color: var(--brand-orange);
    text-transform: uppercase;
  }
  .brand-square {
    width: 44px;
    height: 44px;
    background: var(--brand-orange);
  }
  .card-front {
    background: var(--card-white);
    color: var(--brand-orange);
    font-family: "Jost", sans-serif;
    text-align: center;
    padding-top: 62px;
  }
  .person-name {
    font-family: "Poppins", sans-serif;
    font-weight: 800;
    font-size: 58px;
    line-height: 1;
    letter-spacing: 1px;
  }
  .person-title {
    font-size: 29px;
    font-weight: 400;
    letter-spacing: 1px;
    margin-top: 6px;
  }
  .person-contact {
    font-size: 19px;
    letter-spacing: 1px;
    margin-top: 10px;
  }
  .person-contact .mobile { font-style: italic; }
  .divider {
    width: 410px;
    height: 1px;
    background: var(--brand-orange);
    margin: 22px auto 24px;
  }
  .company-details {
    font-size: 17px;
    letter-spacing: 1.5px;
    line-height: 1.55;
  }
</style>
</head>
<body>
<main class="canvas">
  <section class="card card-back">
    <div class="brand-name"><span class="brand-square"></span>Korrim</div>
  </section>
  <section class="card card-front">
    <h1 class="person-name">Darren Holt</h1>
    <p class="person-title">Machinery Sales Manager</p>
    <p class="person-contact">darren@korrim.com.au &nbsp;|&nbsp; <span class="mobile">xxxx xxx xxx</span></p>
    <div class="divider"></div>
    <div class="company-details">
      <p>48 Ferrow St Brookfield Park, QLD 4172 Australia</p>
      <p>1300 555 018 &nbsp;|&nbsp; +61 7 3900 0142</p>
      <p>www.korrim.com.au</p>
    </div>
  </section>
</main>
</body>
</html>
```